Bellwood Advisors
Name of the Person: Miranda Holloway President
Address 427 Linden Grove Road New York N.Y 10135
Tel: 212 555 0193
Cell: 917 555 02 47
Email:tlandrinc@quorvane.com

Please use the logo idea of Pelvarine Change the sense of the arrow do it from right to left
Pantone color for the logo 300 U
For the word strategist use 300U
Please use same fonts or very similar as the one use in Pelvarine
Please use same lay out as Pelvarine if you can

Industry/Entity Type

Consulting

Logo Text

TL&R CONSULTING Inc

```html
<!DOCTYPE html>
<html lang="en">
<head>
<meta charset="utf-8">
<title>TL&amp;R Consulting – Business Card</title>
<link rel="stylesheet" href="https://fonts.googleapis.com/css2?family=Raleway:wght@400;500&display=swap">
<style>
  :root {
    --brand-blue: #2079bd;
    --ink: #1e1e1e;
    --muted-grey: #9b9b9b;
    --card-border: #8c8c8c;
    --paper: #ffffff;
  }
  html, body {
    margin: 0;
    padding: 0;
    width: 1200px;
    height: 1000px;
    overflow: hidden;
    background: var(--paper);
    font-family: "Raleway", Arial, sans-serif;
  }
  .canvas {
    position: relative;
    width: 1200px;
    height: 1000px;
  }
  .card {
    position: absolute;
    left: 193px;
    top: 221px;
    width: 838px;
    height: 542px;
    border: 1px solid var(--card-border);
    background: var(--paper);
  }
  .company {
    position: absolute;
    left: 34px;
    top: 150px;
    display: flex;
    align-items: center;
    gap: 12px;
  }
  .company-dot {
    width: 14px;
    height: 14px;
    border-radius: 50%;
    background: var(--brand-blue);
    flex: none;
  }
  .company-name {
    margin: 0;
    font-size: 26px;
    font-weight: 500;
    color: var(--ink);
    white-space: nowrap;
  }
  .person {
    position: absolute;
    right: 26px;
    top: 206px;
    text-align: right;
  }
  .person-name {
    margin: 0;
    font-size: 43px;
    font-weight: 500;
    color: var(--ink);
    line-height: 1.1;
    letter-spacing: -0.3px;
  }
  .person-title {
    margin: 0;
    font-size: 21px;
    font-weight: 500;
    color: var(--brand-blue);
    line-height: 1.2;
  }
  .contact {
    position: absolute;
    left: 31px;
    top: 388px;
    margin: 0;
    padding: 0;
    list-style: none;
    font-size: 21px;
    font-weight: 500;
    color: var(--ink);
    line-height: 29.5px;
  }
  .tagline {
    position: absolute;
    right: 26px;
    top: 448px;
    width: 200px;
    height: 50px;
  }
  .tagline-lead {
    position: absolute;
    left: 0;
    top: 0;
    font-size: 24px;
    font-weight: 400;
    color: var(--muted-grey);
    letter-spacing: 0.2px;
    line-height: 1;
  }
  .tagline-accent {
    position: absolute;
    right: 0;
    top: 21px;
    font-size: 24px;
    font-weight: 500;
    color: var(--brand-blue);
    line-height: 1;
  }
</style>
</head>
<body>
  <div class="canvas">
    <section class="card">
      <div class="company">
        <span class="company-dot" aria-hidden="true"></span>
        <p class="company-name">TL&amp;R Consulting Inc</p>
      </div>

      <div class="person">
        <h1 class="person-name">Miranda Holloway</h1>
        <p class="person-title">President</p>
      </div>

      <ul class="contact">
        <li>Address: 427 Linden Grove Road New York N.Y 10135</li>
        <li>Tel: 212 555 0193</li>
        <li>Cell: 917 555 02 47</li>
        <li>Email: tlandrinc@quorvane.com</li>
      </ul>

      <div class="tagline">
        <span class="tagline-lead">BELLWOOD</span>
        <span class="tagline-accent">advisors</span>
      </div>
    </section>
  </div>
</body>
</html>
```